"Cork Hollow Excursions" is a top notch Santa Barbara County Wine Tour company.

We provide scenic, boutique and custom wine tours. I need the card to be clean and classy. I will provide our logo. I would like the logo to cover the back side of the card as an option and would like to see a couple color options other then our signature green and gold. I would like to see some creative options and let the designers come up with options.
I need cards for myself and my team. The final design should communicate "An authentic and boutique wine tour experience"
Please use my website for reference www.corkhollowexcursions.com

Target Market(s)

We have a wide range of clients from millennials to baby boomers

Industry/Entity Type

Tour

Contact Information for Business Card

Contact info:
Dale Munford
805-291-6384
info@corkhollowexcursions.com
corkhollowexcursions.com

Colors

Designer to choose colors to be used in the design.

Requirements
Must have
• my logo
Nice to have
• *I would like to have the backside side with the logo and the company statement
• "An authentic and boutique wine tour experience" as an option.
• *I would also like to see what the designers can create!
• *I would like to see an option that incorporates or social: snapgrid, rovia, route scout
Should not have
• I do not want it too busy.

```html
<!DOCTYPE html>
<html lang="en">
<head>
<meta charset="utf-8">
<title>Cork Hollow Excursions – Business Card</title>
<link rel="stylesheet" href="https://fonts.googleapis.com/css2?family=Noto+Serif:wght@400;700&display=swap">
<style>
  :root {
    --stage: #ece7df;
    --card-white: #ffffff;
    --vine-green: #0e5c30;
    --vine-green-deep: #0a4a26;
    --tan: #d9a98a;
    --ink-light: #ffffff;
    --shadow: rgba(40, 30, 20, 0.18);
  }
  * { box-sizing: border-box; margin: 0; padding: 0; }
  html, body {
    width: 1200px;
    height: 800px;
    overflow: hidden;
    background: var(--stage);
  }
  .canvas {
    width: 1200px;
    height: 800px;
    display: flex;
    align-items: center;
    justify-content: center;
    gap: 60px;
  }
  .card {
    position: relative;
    width: 500px;
    height: 286px;
    border-radius: 4px;
    overflow: hidden;
    box-shadow: 0 10px 28px var(--shadow);
  }

  /* Front: brand side */
  .card-front {
    background: var(--card-white);
    display: flex;
    align-items: center;
    justify-content: center;
    gap: 14px;
  }
  .brand-mark {
    width: 22px;
    height: 22px;
    background: var(--vine-green);
  }
  .brand-name {
    font-family: "Noto Serif", serif;
    font-weight: 700;
    font-size: 28px;
    line-height: 1;
    color: var(--vine-green);
  }

  /* Back: contact side */
  .card-back {
    background: var(--vine-green);
  }
  .contact-row {
    position: absolute;
    left: 34px;
    right: 20px;
    top: 80px;
    height: 66px;
    display: flex;
    align-items: center;
  }
  .person-name {
    font-family: "Noto Serif", serif;
    font-weight: 700;
    font-size: 21px;
    line-height: 1;
    color: var(--ink-light);
    letter-spacing: 0.3px;
    white-space: nowrap;
  }
  .person-name .first { color: var(--tan); }
  .divider {
    flex: 0 0 1px;
    align-self: stretch;
    margin: 0 18px;
    background: var(--ink-light);
  }
  .contact-list {
    list-style: none;
    font-family: "Noto Serif", serif;
    font-size: 13.5px;
    line-height: 19px;
    color: var(--ink-light);
    white-space: nowrap;
  }
  .social-band {
    position: absolute;
    left: 0;
    right: 0;
    top: 212px;
    height: 46px;
    background: var(--tan);
    display: flex;
    align-items: center;
    justify-content: center;
    gap: 26px;
  }
  .social-item {
    display: flex;
    align-items: center;
    gap: 6px;
    font-family: "Noto Serif", serif;
    font-weight: 700;
    font-size: 13px;
    color: var(--vine-green-deep);
  }
  .social-item::before {
    content: "";
    width: 9px;
    height: 9px;
    border-radius: 50%;
    background: var(--vine-green-deep);
  }
</style>
</head>
<body>
  <main class="canvas">
    <section class="card card-front">
      <span class="brand-mark"></span>
      <p class="brand-name">Cork Hollow Excursions</p>
    </section>

    <section class="card card-back">
      <div class="contact-row">
        <h1 class="person-name"><span class="first">DALE</span> MUNFORD</h1>
        <span class="divider"></span>
        <ul class="contact-list">
          <li>805-291-6384</li>
          <li>info@corkhollowexcursions.com</li>
          <li>corkhollowexcursions.com</li>
        </ul>
      </div>
      <div class="social-band">
        <span class="social-item">route scout</span>
        <span class="social-item">snapgrid</span>
        <span class="social-item">rovia</span>
      </div>
    </section>
  </main>
</body>
</html>
```